Consumer and commercial IOT solutions (Internet Of Things)

We are a startup and are looking for business cards with logo. The logo will appear on all of our media as well as our ecommerce site and social sites that have yet to be developed. We want to present a fresh face on a high tech company that innovates at every turn. You can read about our solutions on our information only web site www.plorbaxsystems.net - We have some wording we would like used on our business cards but there is no place for this except for here. The company name is "RM Industrial IOT" I have some samples of logos I am interested in seeing but I will let your team make the initial presentations

```html
<!DOCTYPE html>
<html lang="en">
<head>
<meta charset="utf-8">
<title>RM Industrial IOT – Business Card</title>
<link href="https://fonts.googleapis.com/css2?family=Arimo:wght@400;700&display=swap" rel="stylesheet">
<style>
  :root {
    --backdrop: #d6d4d5;
    --orange: #ec8c35;
    --charcoal: #202020;
    --white: #ffffff;
  }
  * { margin: 0; padding: 0; box-sizing: border-box; }
  html, body {
    width: 1075px;
    height: 1200px;
    overflow: hidden;
    background: var(--backdrop);
    font-family: "Arimo", Arial, sans-serif;
  }
  .card {
    position: absolute;
    left: 208px;
    width: 662px;
    border-radius: 24px;
    overflow: hidden;
  }
  .card--front { top: 187px; height: 396px; background: var(--orange); }
  .card--back  { top: 640px; height: 391px; background: var(--charcoal); }

  .front-art { position: absolute; inset: 0; }

  .identity { position: absolute; left: 34px; top: 52px; color: var(--white); }
  .identity__name { font-size: 26px; font-weight: 700; letter-spacing: 0.2px; line-height: 1; }
  .identity__role { font-size: 18px; font-weight: 400; margin-top: 4px; }

  .contacts { position: absolute; left: 34px; top: 158px; list-style: none; color: var(--white); }
  .contacts li {
    display: flex; align-items: center; gap: 6px;
    font-size: 17.5px; line-height: 23.5px;
  }
  .contacts svg { width: 17px; height: 17px; flex: none; }

  .address {
    position: absolute; left: 34px; top: 292px;
    color: var(--white); font-size: 18px; line-height: 23px; font-style: normal;
  }

  .front-name {
    position: absolute; left: 271px; top: 12px; width: 372px; height: 372px;
    display: flex; align-items: center; justify-content: center;
    color: var(--white); font-size: 30px; font-weight: 700; text-align: center; line-height: 1.2;
  }

  .brand-lockup {
    position: absolute; left: 107px; top: 134px;
    display: flex; align-items: center; gap: 26px;
  }
  .brand-lockup__circle {
    width: 120px; height: 120px; border-radius: 50%;
    border: 5px solid var(--orange); flex: none;
  }
  .brand-lockup__name { color: var(--white); font-size: 38px; font-weight: 700; white-space: nowrap; }
</style>
</head>
<body>

<section class="card card--front">
  <svg class="front-art" width="662" height="396" viewBox="0 0 662 396" aria-hidden="true">
    <rect x="457" y="0" width="205" height="396" fill="var(--charcoal)"/>
    <circle cx="457" cy="198" r="200" fill="var(--orange)"/>
    <circle cx="457" cy="198" r="186" fill="var(--charcoal)"/>
  </svg>

  <div class="identity">
    <h1 class="identity__name">DANIEL MERCER</h1>
    <p class="identity__role">Managing Director</p>
  </div>

  <ul class="contacts">
    <li>
      <svg viewBox="0 0 24 24" fill="none" stroke="currentColor" stroke-width="2"><path d="M5 3h4l2 5-3 2a12 12 0 0 0 6 6l2-3 5 2v4a2 2 0 0 1-2 2A18 18 0 0 1 3 5a2 2 0 0 1 2-2z"/></svg>
      044-555 018 274
    </li>
    <li>
      <svg viewBox="0 0 24 24" fill="currentColor"><path d="M2 5h20v14H2z" /><path d="M2 5l10 8 10-8" fill="none" stroke="var(--orange)" stroke-width="1.8"/></svg>
      hello@plorbaxsystems.net
    </li>
    <li>
      <svg viewBox="0 0 24 24" fill="none" stroke="currentColor" stroke-width="1.8"><circle cx="12" cy="12" r="10"/><path d="M2 12h20M12 2c3 3 3 17 0 20M12 2c-3 3-3 17 0 20"/></svg>
      www.plorbaxsystems.net
    </li>
  </ul>

  <address class="address">
    88, Harlow Trade Park Road<br>
    30917, Westmark
  </address>

  <p class="front-name">RM Industrial IOT</p>
</section>

<section class="card card--back">
  <div class="brand-lockup">
    <span class="brand-lockup__circle"></span>
    <span class="brand-lockup__name">RM Industrial IOT</span>
  </div>
</section>

</body>
</html>
```